This is a laser engraving business. I’m looking for a business card that includes a minimalist laser logo/design with the company name Brindle Crafts and telephone number 321-555-0148 and email brindlecrafts@mailbox.example

Industry/Entity Type

Laser engraving

Contact Information for Business Card

Laser logo/design that represents laser engraving

```html
<!DOCTYPE html>
<html lang="en">
<head>
<meta charset="utf-8">
<title>Brindle Crafts — Business Card</title>
<link href="https://fonts.googleapis.com/css2?family=Montserrat:wght@600;700&family=Oswald:wght@500&family=Roboto:wght@400;700&display=swap" rel="stylesheet">
<style>
  :root {
    --backdrop: #b7b7b7;
    --ink: #000000;
    --paper: #ffffff;
    --art-light: #d9d9d9;
    --art-dark: #5a5a5a;
    --shadow: rgba(0, 0, 0, 0.55);
  }
  html, body {
    margin: 0;
    padding: 0;
    width: 1075px;
    height: 1200px;
    overflow: hidden;
    background: var(--backdrop);
  }
  .sheet {
    position: relative;
    width: 1075px;
    height: 1200px;
  }
  .card {
    position: absolute;
    left: 206px;
    width: 663px;
    height: 395px;
    box-shadow: 3px 3px 3px var(--shadow);
  }
  .card svg { display: block; width: 100%; height: 100%; }
  .card--front { top: 187px; background: var(--paper); }
  .card--back { top: 637px; background: var(--ink); }

  .brand-vertical {
    font-family: "Montserrat", sans-serif;
    font-weight: 700;
    font-size: 38px;
    fill: var(--ink);
  }
  .phone {
    font-family: "Oswald", sans-serif;
    font-weight: 500;
    font-size: 62px;
    fill: var(--paper);
  }
  .email {
    font-family: "Roboto", sans-serif;
    font-size: 21px;
    fill: var(--ink);
  }
  .email-label { font-weight: 700; }
  .brand-name {
    font-family: "Montserrat", sans-serif;
    font-weight: 600;
    font-size: 38px;
    fill: var(--paper);
  }
</style>
</head>
<body>
<main class="sheet">

  <section class="card card--front" aria-label="Business card front">
    <svg viewBox="0 0 738 440" xmlns="http://www.w3.org/2000/svg">
      <defs>
        <linearGradient id="artTone" x1="0" y1="0" x2="1" y2="0">
          <stop offset="0" stop-color="var(--art-dark)"/>
          <stop offset="1" stop-color="var(--art-light)"/>
        </linearGradient>
      </defs>

      <text class="brand-vertical" x="0" y="0" text-anchor="middle" dominant-baseline="central"
            transform="translate(100 232) rotate(-90)">BRINDLE CRAFTS</text>

      <rect class="laser-art" x="214" y="0" width="110" height="440" fill="url(#artTone)"
            role="img" aria-label="Laser beam illustration radiating from an engraving point"/>

      <polygon class="phone-band" fill="var(--ink)"
               points="356,174 738,174 738,262 356,262 342,242 336,220 342,198"/>
      <text class="phone" x="387" y="244" textLength="305" lengthAdjust="spacingAndGlyphs">321-555-0148</text>

      <text class="email" x="356" y="385" textLength="341" lengthAdjust="spacingAndGlyphs"><tspan class="email-label">E:</tspan> brindlecrafts@mailbox.example</text>
    </svg>
  </section>

  <section class="card card--back" aria-label="Business card back">
    <svg viewBox="0 0 738 440" xmlns="http://www.w3.org/2000/svg">
      <rect class="brand-mark" x="154" y="172" width="96" height="96" fill="var(--paper)"/>
      <rect class="brand-divider" x="287" y="159" width="2" height="124" fill="var(--paper)"/>
      <text class="brand-name" x="323" y="211">BRINDLE</text>
      <text class="brand-name" x="323" y="261">CRAFTS</text>
    </svg>
  </section>

</main>
</body>
</html>
```